Unternehmen für Wimpernverlängerung & -lifting benötigt Flyer-Design
Zielgruppe
Wimpernverlängerung, Wimpernlifting, Permanent Make-Up, Microblading, BB Glow, Hyaluron Pen
Aufgabenstellung
es soll eine preisliste werden, ich möchte die preise selbst einsetzen
produkte:
Wimpernverlängerung:
Natural Look
Auffüllen bis 1-2 Wochen
Auffüllen bis 3-4 Wochen
Ab der 5. Woche Neupreis
Volumen Look
Wimpernlifting inkl. färben
Microblading
Permanent Make-Up:
Powder Brows
Powder Brows Combo (Härchen&Shading)
Wimpernkranzverdichtung
Lidstrich dekorativ
Aquarelle Lips
Lippen Vollschattierung
BB Glow
Hyaluron Pen
Termine nach Vereinbarung

```html
<!DOCTYPE html>
<html lang="de">
<head>
<meta charset="utf-8">
<title>Glanzblick – Preisliste Flyer</title>
<link rel="stylesheet" href="https://fonts.googleapis.com/css2?family=Cinzel:wght@400;600&family=Comfortaa:wght@400;700&family=Fredoka:wght@600&display=swap">
<style>
:root{
  --purple:#8a4a8c;
  --purple-dark:#6e3470;
  --pink:#ee9fca;
  --pink-soft:#f6c9df;
  --paper:#fbf3f6;
  --line:#e8c3d5;
  --ink:#6a5a66;
  --stage:#ececec;
  --serif:'Cinzel', serif;
  --sans:'Comfortaa', sans-serif;
}
*{box-sizing:border-box;margin:0;padding:0}
html,body{width:1200px;height:2400px;overflow:hidden}
body{background:var(--stage);position:relative;font-family:var(--sans);color:var(--ink)}

.side-label{position:absolute;left:880px;font-family:'Fredoka', sans-serif;font-weight:600;font-size:40px;letter-spacing:2px;color:var(--purple)}
.side-label.front{top:110px}
.side-label.back{top:1280px}

.flyer{position:absolute;left:300px;width:540px;height:1130px;background:var(--paper);overflow:hidden;box-shadow:0 6px 24px rgba(0,0,0,.12)}
.flyer.front{top:50px}
.flyer.back{top:1220px}

.hero-photo{position:absolute;left:0;top:0;width:540px;height:440px}
.front .hero-photo{background:linear-gradient(135deg,#f3ddd2 0%,#e8c0ac 45%,#f8ece6 75%,#d9b8a6 100%)}
.back .hero-photo{background:linear-gradient(120deg,#f4b6d3 0%,#f7e6e0 35%,#efd2c6 65%,#f2a7cc 100%)}

.hero-swoosh{position:absolute;left:0;top:300px;width:540px;height:170px}

.brand{position:absolute;left:30px;top:40px;font-family:var(--serif);font-size:34px;font-weight:400;color:var(--purple);letter-spacing:2px}

.call-badge{position:absolute;left:360px;top:250px;width:160px;height:160px;border-radius:50%;background:var(--pink-soft);border:6px solid #fff;box-shadow:0 0 0 3px var(--purple);display:flex;flex-direction:column;align-items:center;justify-content:center;text-align:center;color:var(--purple)}
.call-badge svg{width:22px;height:22px;margin-bottom:4px}
.call-badge .call-label{font-size:13px;letter-spacing:3px;color:#fff}
.call-badge .call-number{font-size:19px;font-weight:700;line-height:1.1}

.section-title{position:absolute;left:50%;transform:translateX(-50%);padding:10px 26px;border-radius:24px;background:var(--purple);color:#fff;font-family:var(--serif);font-size:20px;letter-spacing:2px;white-space:nowrap;box-shadow:0 0 0 3px var(--pink-soft)}

.price-group{position:absolute;left:30px;right:30px}
.group-tab{position:absolute;left:0;top:0;bottom:0;width:28px;background:var(--pink);color:#fff;font-size:10px;font-weight:700;letter-spacing:1px;writing-mode:vertical-rl;transform:rotate(180deg);display:flex;align-items:center;justify-content:center;text-transform:uppercase}
.price-box{position:absolute;left:40px;right:0;top:0;bottom:0;border:1px solid var(--line);background:#fff9fb;padding:14px 16px;display:flex;flex-direction:column;justify-content:space-around}
.price-row{display:flex;align-items:baseline;font-size:13px;text-transform:uppercase;letter-spacing:.5px}
.price-row b{font-weight:700;color:#5a4a56}
.price-row .leader{flex:1;border-bottom:1px dotted #c9a9ba;margin:0 8px}
.price-row .price{font-weight:700;color:#5a4a56}

.footer-swoosh{position:absolute;left:0;bottom:0;width:540px;height:200px}
.front .footer-swoosh{height:180px}
.round-photo{position:absolute;left:28px;bottom:30px;width:150px;height:150px;border-radius:50%;border:6px solid #fff;box-shadow:0 0 0 3px var(--purple)}
.front .round-photo{background:radial-gradient(circle at 50% 40%,#a88a90 0%,#5a3a48 55%,#2e2228 100%)}
.back .round-photo{background:linear-gradient(160deg,#f2ede8 0%,#d9cfc6 50%,#8f7f73 100%)}
.photo-pill{position:absolute;padding:5px 14px;border-radius:14px;background:var(--purple);color:#fff;font-family:var(--serif);font-size:12px;letter-spacing:1px;border:2px solid #fff;white-space:nowrap}
.front .photo-pill{left:80px;bottom:24px}
.back .photo-pill{left:30px;bottom:160px}

.greeting{position:absolute;left:225px;right:24px;top:1022px}
.greeting h3{font-size:15px;font-weight:700;color:var(--purple);text-transform:uppercase;margin-bottom:5px;white-space:nowrap}
.greeting p{font-size:12px;line-height:1.45;color:#9a8a94}

.contact{position:absolute;left:200px;right:24px;bottom:30px}
.contact h3{font-size:15px;font-weight:700;color:var(--purple);text-transform:uppercase;margin-bottom:5px}
.contact .who{font-size:11px;color:#7a6a76;margin-bottom:8px}
.contact .who b{color:#5a4a56}
.contact ul{list-style:none;display:grid;grid-template-columns:1fr 1fr;gap:6px 10px;font-size:11px;color:#8a7a86;margin-bottom:10px}
.contact li{display:flex;align-items:center;gap:6px}
.contact .dot{width:12px;height:12px;border-radius:50%;background:var(--purple);flex:none;display:flex;align-items:center;justify-content:center}
.contact .dot svg{width:8px;height:8px}
.web-pill{display:block;text-align:center;padding:6px 0;border-radius:14px;background:var(--purple);color:#fff;font-family:var(--serif);font-size:13px;letter-spacing:1px}
</style>
</head>
<body>

<div class="side-label front">VORDERSEITE</div>
<div class="side-label back">RÜCKSEITE</div>

<!-- Vorderseite -->
<section class="flyer front">
  <div class="hero-photo" role="img" aria-label="Foto: Wimpernverlängerung mit Pinzette an geschlossenem Auge"></div>
  <svg class="hero-swoosh" viewBox="0 0 540 170" preserveAspectRatio="none" aria-hidden="true">
    <path d="M0 170 L0 128 Q280 70 540 40 L540 170 Z" fill="#fbf3f6"/>
    <path d="M0 118 Q260 55 540 -10 L540 18 Q270 72 0 128 Z" fill="#8a4a8c"/>
    <path d="M0 136 Q280 78 540 48" stroke="#ee9fca" stroke-width="5" fill="none"/>
  </svg>
  <div class="brand">GLANZBLICK</div>
  <div class="call-badge">
    <svg viewBox="0 0 24 24"><path fill="#8a4a8c" d="M6.6 10.8a15 15 0 0 0 6.6 6.6l2.2-2.2a1 1 0 0 1 1-.25 11.4 11.4 0 0 0 3.6.57 1 1 0 0 1 1 1V20a1 1 0 0 1-1 1A17 17 0 0 1 3 4a1 1 0 0 1 1-1h3.5a1 1 0 0 1 1 1c0 1.25.2 2.45.57 3.6a1 1 0 0 1-.25 1z"/></svg>
    <span class="call-label">TERMINE:</span>
    <span class="call-number">0176 555<br>01934</span>
  </div>

  <h2 class="section-title" style="top:470px">WIMPERNVERLÄNGERUNG:</h2>

  <div class="price-group" style="top:545px;height:130px">
    <div class="group-tab">Natural Look</div>
    <div class="price-box">
      <div class="price-row">Auffüllen | bis&nbsp;<b>1-2 Wochen</b><span class="leader"></span><span class="price">50,00€</span></div>
      <div class="price-row">Auffüllen | bis&nbsp;<b>3-4 Wochen</b><span class="leader"></span><span class="price">75,00€</span></div>
      <div class="price-row">Ab der&nbsp;<b>5. Woche</b>&nbsp;Neupreis<span class="leader"></span><span class="price">95,00€</span></div>
    </div>
  </div>

  <div class="price-group" style="top:695px;height:130px">
    <div class="group-tab">Volumen Look</div>
    <div class="price-box">
      <div class="price-row">Auffüllen | bis&nbsp;<b>1-2 Wochen</b><span class="leader"></span><span class="price">50,00€</span></div>
      <div class="price-row">Auffüllen | bis&nbsp;<b>3-4 Wochen</b><span class="leader"></span><span class="price">75,00€</span></div>
      <div class="price-row">Ab der&nbsp;<b>5. Woche</b>&nbsp;Neupreis<span class="leader"></span><span class="price">95,00€</span></div>
    </div>
  </div>

  <div class="price-group" style="top:845px;height:95px">
    <div class="group-tab">Specials</div>
    <div class="price-box">
      <div class="price-row"><b>Wimpernlifting</b>&nbsp;inkl. Färben<span class="leader"></span><span class="price">50,00€</span></div>
      <div class="price-row"><b>Microblading</b><span class="leader"></span><span class="price">75,00€</span></div>
    </div>
  </div>

  <svg class="footer-swoosh" viewBox="0 0 540 180" aria-hidden="true">
    <path d="M120 62 Q330 8 540 2" stroke="#ee9fca" stroke-width="9" fill="none"/>
    <path d="M140 78 Q330 24 540 16" stroke="#8a4a8c" stroke-width="3" fill="none"/>
    <path d="M0 180 L0 130 Q40 155 110 180 Z" fill="#8a4a8c"/>
    <path d="M30 180 Q80 162 120 180 Z" fill="#ee9fca"/>
  </svg>
  <div class="round-photo" role="img" aria-label="Porträtfoto der Stylistin"></div>
  <div class="photo-pill">MIRABEL TOSCH</div>
  <div class="greeting">
    <h3>Ich freue mich auf euch</h3>
    <p>Mein Name ist Mirabel Tosch und ich bin seit 2014 zertifizierte Lash-Stylistin und seit 2017 Permanent Make-Up und Microblading Stylistin.</p>
  </div>
</section>

<!-- Rückseite -->
<section class="flyer back">
  <div class="hero-photo" role="img" aria-label="Foto: Behandlung mit rosa Handschuhen und Pinzette am Auge"></div>
  <svg class="hero-swoosh" viewBox="0 0 540 170" preserveAspectRatio="none" aria-hidden="true">
    <path d="M0 170 L0 128 Q280 70 540 40 L540 170 Z" fill="#fbf3f6"/>
    <path d="M0 118 Q260 55 540 -10 L540 18 Q270 72 0 128 Z" fill="#8a4a8c"/>
    <path d="M0 136 Q280 78 540 48" stroke="#ee9fca" stroke-width="5" fill="none"/>
  </svg>
  <div class="call-badge">
    <svg viewBox="0 0 24 24"><path fill="#8a4a8c" d="M6.6 10.8a15 15 0 0 0 6.6 6.6l2.2-2.2a1 1 0 0 1 1-.25 11.4 11.4 0 0 0 3.6.57 1 1 0 0 1 1 1V20a1 1 0 0 1-1 1A17 17 0 0 1 3 4a1 1 0 0 1 1-1h3.5a1 1 0 0 1 1 1c0 1.25.2 2.45.57 3.6a1 1 0 0 1-.25 1z"/></svg>
    <span class="call-label">TERMINE:</span>
    <span class="call-number">0176 555<br>01934</span>
  </div>

  <h2 class="section-title" style="top:460px">PERMANENT MAKE-UP:</h2>

  <div class="price-group" style="top:535px;height:215px">
    <div class="group-tab">Permanent Make-Up</div>
    <div class="price-box">
      <div class="price-row">Powder Brows<span class="leader"></span><span class="price">50,00€</span></div>
      <div class="price-row">Powder Brows Combo (Härchen&amp;Shading)<span class="leader"></span><span class="price">75,00€</span></div>
      <div class="price-row">Wimpernkranzverdichtung<span class="leader"></span><span class="price">95,00€</span></div>
      <div class="price-row">Lidstrich dekorativ<span class="leader"></span><span class="price">50,00€</span></div>
      <div class="price-row">Aquarelle Lips<span class="leader"></span><span class="price">75,00€</span></div>
      <div class="price-row">Lippen Vollschattierung<span class="leader"></span><span class="price">95,00€</span></div>
    </div>
  </div>

  <h2 class="section-title" style="top:775px">WEITERE LEISTUNGEN:</h2>

  <div class="price-group" style="top:845px;height:90px">
    <div class="group-tab">Specials</div>
    <div class="price-box">
      <div class="price-row">BB Glow<span class="leader"></span><span class="price">50,00€</span></div>
      <div class="price-row">Hyaluron Pen<span class="leader"></span><span class="price">75,00€</span></div>
    </div>
  </div>

  <svg class="footer-swoosh" viewBox="0 0 540 200" preserveAspectRatio="none" aria-hidden="true">
    <path d="M130 60 Q330 0 540 -5" stroke="#ee9fca" stroke-width="10" fill="none"/>
    <path d="M150 80 Q330 20 540 12" stroke="#8a4a8c" stroke-width="3" fill="none"/>
    <path d="M0 200 L0 150 Q40 175 110 200 Z" fill="#8a4a8c"/>
    <path d="M30 200 Q80 180 120 200 Z" fill="#ee9fca"/>
  </svg>
  <div class="round-photo" role="img" aria-label="Foto: Behandlungsraum des Studios"></div>
  <div class="photo-pill">ICH FREUE MICH</div>
  <div class="contact">
    <h3>Termine nach Vereinbarung</h3>
    <p class="who"><b>Mirabel Tosch</b> | 87400 Musterhofen/Auen</p>
    <ul>
      <li><span class="dot"><svg viewBox="0 0 24 24"><path fill="#fff" d="M6.6 10.8a15 15 0 0 0 6.6 6.6l2.2-2.2a1 1 0 0 1 1-.25 11.4 11.4 0 0 0 3.6.57 1 1 0 0 1 1 1V20a1 1 0 0 1-1 1A17 17 0 0 1 3 4a1 1 0 0 1 1-1h3.5a1 1 0 0 1 1 1c0 1.25.2 2.45.57 3.6a1 1 0 0 1-.25 1z"/></svg></span>0176 555 01934</li>
      <li><span class="dot"></span>glanzblick_studio</li>
      <li><span class="dot"></span>glanzblick25</li>
    </ul>
    <span class="web-pill">WWW.GLANZBLICK-STUDIO.DE</span>
  </div>
</section>

</body>
</html>
```